Visitenkarten-Design für Persisches Restaurant
Zielgruppe
persisches Restaurant, suche ein Hochwertiges Design für internationale Kunden
Aufgabenstellung
möchte eine hochwertige und elegante visitenkarte
auf der Vorderseite sollte das Logo sein und auf der Rückseite Öffnungszeit, Adresse, Tel. E-Mail und homepage

```html
<!DOCTYPE html>
<html lang="de">
<head>
<meta charset="utf-8">
<title>Dalira – Visitenkarte</title>
<link href="https://fonts.googleapis.com/css2?family=Crimson+Text:wght@400;600&display=swap" rel="stylesheet">
<style>
  :root {
    --page: #ffffff;
    --card: #dcdddd;
    --ink: #1a1a1a;
    --frame: #111111;
    --shadow: rgba(0,0,0,0.28);
  }
  html, body {
    margin: 0;
    padding: 0;
    width: 738px;
    height: 1200px;
    overflow: hidden;
    background: var(--page);
  }
  .canvas {
    position: relative;
    width: 738px;
    height: 1200px;
    font-family: "Crimson Text", "Times New Roman", serif;
    color: var(--ink);
  }
  .card {
    position: absolute;
    top: 161px;
    width: 189px;
    height: 332px;
    box-sizing: border-box;
    background: var(--card);
    box-shadow: 0 2px 8px var(--shadow);
  }
  .card--front {
    left: 136px;
  }
  .card--back {
    left: 416px;
    width: 186px;
    border: 7px solid var(--frame);
    text-align: center;
    font-size: 9.6px;
    line-height: 1.45;
  }
  .brand {
    position: absolute;
    left: 0;
    right: 0;
    top: 150px;
    display: flex;
    align-items: center;
    justify-content: center;
    gap: 5px;
  }
  .brand__mark {
    width: 11px;
    height: 11px;
    border-radius: 50%;
    background: var(--ink);
  }
  .brand__name {
    font-size: 24px;
    font-weight: 600;
    letter-spacing: 0.5px;
    line-height: 1;
  }
  .contact {
    position: absolute;
    left: 0;
    right: 0;
  }
  .contact--address { top: 38px; }
  .contact--reach { top: 76px; }
  .contact p { margin: 0; }
  .divider {
    position: absolute;
    left: 28px;
    top: 144px;
    width: 116px;
    height: 10px;
  }
  .hours {
    position: absolute;
    left: 46px;
    top: 176px;
    border-collapse: collapse;
    font-size: 9.6px;
  }
  .hours td {
    padding: 0;
    height: 17px;
    text-align: left;
  }
  .hours .day { width: 21px; }
</style>
</head>
<body>
<div class="canvas">
  <section class="card card--front" aria-label="Vorderseite">
    <div class="brand">
      <span class="brand__mark"></span>
      <span class="brand__name">DALIRA</span>
    </div>
  </section>

  <section class="card card--back" aria-label="Rückseite">
    <div class="contact contact--address">
      <p>Lindenhofweg 14</p>
      <p>60325 Frankfurt am Main</p>
    </div>
    <div class="contact contact--reach">
      <p>069 / 48 21 90</p>
      <p>info@dalira-kueche.de</p>
      <p>www.dalira-kueche.de</p>
    </div>
    <svg class="divider" viewBox="0 0 116 10" aria-hidden="true">
      <line x1="0" y1="5" x2="116" y2="5" stroke="#1a1a1a" stroke-width="0.8"/>
      <circle cx="58" cy="5" r="3.2" fill="var(--card)" stroke="#1a1a1a" stroke-width="1.4"/>
    </svg>
    <table class="hours">
      <tr><td class="day">Mo</td><td>11:30 - 22:30</td></tr>
      <tr><td class="day">D</td><td>11:30 - 22:30</td></tr>
      <tr><td class="day">Mi</td><td>11:30 - 22:30</td></tr>
      <tr><td class="day">D</td><td>11:30 - 22:30</td></tr>
      <tr><td class="day">F</td><td>11:30 - 22:30</td></tr>
      <tr><td class="day">Sa</td><td>12:00 - 22:30</td></tr>
      <tr><td class="day">So</td><td>12:00 - 22:30</td></tr>
    </table>
  </section>
</div>
</body>
</html>
```